Dry Cleaners Pick-up & Delivery Service

We are in the need of a post card design to hand out in public focused in our dry-cleaners pick up and delivery business services. The postcard must include a price list of most common items sent to the dry cleaners on a regular basis along with promotional sign-up deals and specials as advertised on our website. The color palette must match our website's color scheme - www.vorqualin.com - we would like to focus on our free pick-up and free delivery service. The hand out post card should look clean, organized and neat, yet modern in style projecting the cleanliness of the clothing articles that our customer let us take care of saving them time while we take care of this errand for them. All new customers receive a free high quality, heavy duty laundry bag with our business information and are encouraged to request for $10 of free dry cleaning on their first order, no strings attached, just for signing up to our service.We strive to please our customers and invest on them to have more free time on their hands, plain and simple. We also offer law enforcement uniform special, as the area we focus our routes is a high law enforcement residential community. The logo is attached and must be visible in the postcard as well as the website address and phone number 305-472-1946 as these are the main contact forms of clients reaching our business. This is home based business, we have a partnership with a dry cleaners business who does all of our route customers' dry cleaning needs. Our business is all about the marketing, sales and networking with corporate businesses. The postcard handout must have designs of both sides of the post card as well. They will not be used for mailing for the moment being, they will be only used to hand out.

Industry/Entity Type

Dry Cleaning

```html
<!DOCTYPE html>
<html lang="en">
<head>
<meta charset="utf-8">
<title>Vorqualin – Dry Cleaners Pick-up &amp; Delivery Postcard</title>
<link rel="stylesheet" href="https://fonts.googleapis.com/css2?family=Open+Sans:wght@400;600;700;800&family=Archivo+Black&display=swap">
<style>
  :root{
    --bg:#eceae6;
    --card:#ffffff;
    --card-fade:#e6e7e8;
    --ink:#1d1d1d;
    --muted:#555;
    --band:#d9d9d9;
    --slate:#5b6271;
    --green:#6cbf4a;
    --green-dark:#4e9a33;
    --shirt-light:#c9d8ea;
    --shirt-dark:#3d5479;
    --basket:#6b4a33;
    --towel:#8fa595;
  }
  *{box-sizing:border-box;margin:0;padding:0}
  html,body{width:1200px;height:903px;overflow:hidden;background:var(--bg);font-family:"Open Sans",Arial,sans-serif;color:var(--ink)}
  .canvas{position:relative;width:1200px;height:903px}
  .card{position:absolute;background:linear-gradient(180deg,var(--card) 40%,var(--card-fade));box-shadow:4px 6px 12px rgba(0,0,0,.25);overflow:hidden}

  /* Front */
  .card--front{left:280px;top:17px;width:440px;height:570px}
  .photo-shirts{position:absolute;left:0;top:0;width:440px;height:172px;background:linear-gradient(90deg,var(--shirt-light),#eef2f7 25%,var(--shirt-dark) 45%,#8eaad0 65%,#f3f5f8 80%,var(--shirt-light))}
  .service-band{position:absolute;left:0;top:172px;width:440px;height:34px;background:var(--band);font-weight:700;font-size:17px;text-align:center;line-height:34px}
  .brand{font-family:"Open Sans",Arial,sans-serif;font-weight:700;color:var(--ink);display:flex;align-items:center;gap:8px}
  .brand__dot{width:14px;height:14px;border-radius:50%;background:var(--green)}
  .card--front .brand{position:absolute;left:22px;top:245px;font-size:34px}
  .signup-box{position:absolute;left:255px;top:236px;width:166px;height:64px;background:var(--slate);color:#fff;padding:10px 10px;font-weight:700}
  .signup-box__title{font-size:15px;letter-spacing:1px}
  .signup-box__call{font-size:12px}
  .signup-box__call b{font-size:16px}
  .perks{position:absolute;left:30px;top:322px;list-style:none;font-family:"Archivo Black",Arial,sans-serif;font-size:16px;line-height:33px}
  .perks li{display:flex;align-items:center;gap:6px}
  .perks svg{width:16px;height:16px}
  .photo-basket{position:absolute;left:0;bottom:0;width:170px;height:110px;background:linear-gradient(180deg,var(--towel) 0 30%,var(--basket) 30%);border-radius:8px 8px 0 0}
  .coupon{position:absolute;left:215px;top:446px;width:212px;height:120px;background:var(--green);border-radius:6px;padding:6px}
  .coupon__tail{position:absolute;left:20px;top:-20px}
  .coupon__inner{border:1.5px dashed #fff;border-radius:4px;height:100%;padding:24px 10px 6px;color:#111;font-size:10.5px;line-height:13px}
  .coupon__inner b{font-size:14px}
  .coupon__url{display:block;color:#fff;font-weight:700;font-size:13px;text-align:center;margin-top:8px}

  /* Back */
  .card--back{left:734px;top:59px;width:452px;height:576px}
  .card--back .brand{position:absolute;left:24px;top:30px;font-size:32px}
  .back-signup{position:absolute;right:28px;top:38px;font-weight:700}
  .back-signup__title{font-size:17px;letter-spacing:1.5px}
  .back-signup__call{font-size:12px}
  .back-signup__call b{font-size:16px;font-weight:600}
  .pricing-title{position:absolute;left:24px;top:118px;font-size:8.5px;color:var(--muted)}
  .col{position:absolute;top:134px}
  .col--women{left:24px;width:200px}
  .col--men{left:232px;width:196px;border-left:1px solid #555;padding-left:6px;height:266px}
  .col h3{font-size:9px;font-weight:700;margin-bottom:6px}
  .item{display:flex;justify-content:space-between;padding-left:6px;height:18.5px}
  .item__name{font-size:9.5px;font-weight:600;line-height:10px}
  .item__name small{display:block;font-size:5.5px;font-weight:400;color:var(--muted);line-height:7px}
  .item__price{font-size:9.5px;font-weight:600}
  .fine-print{font-size:5px;line-height:6.5px;color:var(--muted);padding-left:6px;margin:12px 0 16px}
  .gap{height:14px}
  .photo-basket--back{width:150px;height:104px}
  .back-url{position:absolute;right:24px;bottom:18px;color:var(--green);font-weight:700;font-size:20px}
</style>
</head>
<body>
<main class="canvas">

  <section class="card card--front" aria-label="Postcard front">
    <div class="photo-shirts" role="img" aria-label="Photo of pressed dress shirts on hangers"></div>
    <div class="service-band">Dry Cleaners Pick up &amp; Delivery Services</div>
    <div class="brand"><span class="brand__dot"></span>Vorqualin</div>
    <div class="signup-box">
      <div class="signup-box__title">SIGN-UP FREE!</div>
      <div class="signup-box__call">CALL <b>305-472-1946</b></div>
    </div>
    <ul class="perks">
      <li><svg viewBox="0 0 16 16"><path d="M2 9l4 4 9-12" fill="none" stroke="#111" stroke-width="2.2"/></svg>FREE PICK-UP!</li>
      <li><svg viewBox="0 0 16 16"><path d="M2 9l4 4 9-12" fill="none" stroke="#111" stroke-width="2.2"/></svg>FREE DELIVERY!</li>
      <li><svg viewBox="0 0 16 16"><path d="M2 9l4 4 9-12" fill="none" stroke="#111" stroke-width="2.2"/></svg>NEXT-DAY SERVICE AVAILABLE!</li>
    </ul>
    <div class="photo-basket" role="img" aria-label="Photo of folded towels in a wicker laundry basket"></div>
    <div class="coupon">
      <svg class="coupon__tail" width="36" height="22" viewBox="0 0 36 22"><path d="M0 0 L36 22 H10 Z" fill="var(--green)"/></svg>
      <div class="coupon__inner">
        <b>$10</b> of free dry cleaning<br>on your first order, no strings attached,<br>just for signing up to our service.
        <span class="coupon__url">www.vorqualin.com</span>
      </div>
    </div>
  </section>

  <section class="card card--back" aria-label="Postcard back">
    <div class="brand"><span class="brand__dot"></span>Vorqualin</div>
    <div class="back-signup">
      <div class="back-signup__title">SIGN-UP FREE!</div>
      <div class="back-signup__call">CALL <b>305-472-1946</b></div>
    </div>
    <div class="pricing-title">DRY CLEANING PRICING:</div>

    <div class="col col--women">
      <h3>WOMEN</h3>
      <div class="item"><span class="item__name">Dress<small>Dry-Cleaned &amp; Pressed</small></span><span class="item__price">$10.95</span></div>
      <div class="item"><span class="item__name">Women Blouse<small>Dry-Cleaned &amp; Pressed</small></span><span class="item__price">$4.95</span></div>
      <div class="item"><span class="item__name">Women Casual Pants/Jeans<small>Dry-Cleaned &amp; Pressed</small></span><span class="item__price">$4.95</span></div>
      <div class="item"><span class="item__name">Skirt - Long<small>Dry-Cleaned &amp; Pressed</small></span><span class="item__price">$6.49</span></div>
      <div class="item"><span class="item__name">Skirt - Short<small>Dry-Cleaned &amp; Pressed</small></span><span class="item__price">$4.95</span></div>
      <div class="item"><span class="item__name">Women Suit<small>2 piece - Dry-Cleaned &amp; Pressed</small></span><span class="item__price">$10.95</span></div>
      <div class="item"><span class="item__name">Women Evening/Formal Dress<small>Subject to surcharge (beads, etc)</small></span><span class="item__price">$28.99</span></div>
      <p class="fine-print">*Items with beads, sequins or trim may carry an added charge.<br>*Leather, suede and fur pieces are priced at drop-off.<br>*Stains are treated with care but removal is not guaranteed.</p>
      <div class="item"><span class="item__name">Pillow Covers<small>Any size</small></span><span class="item__price">$2.99</span></div>
      <div class="item"><span class="item__name">Table Cloths &amp; Runners (Large)</span><span class="item__price">$11.95</span></div>
      <div class="item"><span class="item__name">Table Cloth &amp; Runners (Small)</span><span class="item__price">$9.99</span></div>
    </div>

    <div class="col col--men">
      <h3>MEN</h3>
      <div class="item"><span class="item__name">Men's Shirt (100% cotton)<small>Laundered &amp; Pressed</small></span><span class="item__price">$2.99</span></div>
      <div class="item"><span class="item__name">Men Business Shirt<small>Dry-Cleaned &amp; Pressed</small></span><span class="item__price">$4.50</span></div>
      <div class="item"><span class="item__name">Men Business Pants<small>Dry-Cleaned &amp; Pressed</small></span><span class="item__price">$4.95</span></div>
      <div class="item"><span class="item__name">Men Business Vest<small>Dry-Cleaned &amp; Pressed</small></span><span class="item__price">$4.95</span></div>
      <div class="item"><span class="item__name">Men Pants/Jeans<small>Dry-Cleaned &amp; Pressed</small></span><span class="item__price">$4.95</span></div>
      <div class="item"><span class="item__name">Men Suit<small>2-Piece - Dry-Cleaned &amp; Pressed</small></span><span class="item__price">$10.95</span></div>
      <div class="item"><span class="item__name">3 piece suit<small>Dry-Cleaned &amp; Pressed</small></span><span class="item__price">$15.95</span></div>
      <div class="item"><span class="item__name">Tie<small>Dry-Cleaned &amp; Pressed</small></span><span class="item__price">$3.95</span></div>
      <div class="item"><span class="item__name">Sports Coat/Jacket<small>Dry-Cleaned &amp; Pressed</small></span><span class="item__price">$6.95</span></div>
      <div class="item"><span class="item__name">Men Guayabera<small>Laundered and Pressed</small></span><span class="item__price">$6.99</span></div>
      <div class="gap"></div>
      <div class="item" style="height:34px"><span class="item__name">LAW ENFORCEMENT SPECIAL<small>1 LEO shirt with 1 LEO pair of pants<br>Dry-Cleaned and Pressed</small></span><span class="item__price">$7.99</span></div>
      <div class="item" style="height:30px"><span class="item__name">WASH &amp; FOLD PRICING<small style="font-size:8px;line-height:10px;color:var(--ink)">Regular Clothing Articles</small><small>Displayed pricing is per pound</small></span><span class="item__price">$1.99</span></div>
    </div>

    <div class="photo-basket photo-basket--back" role="img" aria-label="Photo of folded towels in a wicker laundry basket"></div>
    <div class="back-url">www.vorqualin.com</div>
  </section>

</main>
</body>
</html>
```